Business cards — need something that creates “wow” factor

Need a sleek and clean looking business card. Something that is clear and consise. These business cards are for my painting business and hundreds will be placed in the Dallas area between all Halverd Pemberton paint stored. These card really need to stick out! Open to any and all ideas...

Target Market(s)

Residential clientele

Industry/Entity Type

Painting

Contact Information for Business Card

Dorian Vakelby
Owner

382.516.2074

Web: Mesahuepainting.example (still under construction)
Mesahuepainting@mailbox.example

Font styles to use
Sans Serif

Colors

Designer to choose colors to be used in the design.

Requirements
Must have
• My name, number, website, email, Socialpage
• and “100% customer satisfaction guaranteed”
• Socialpage.example/Mesahuepainting/
Nice to have
• Listed services
• Interior/exterior painting
• Drywall repair/texture
• Fence staining/refinishing
• Concrete staining
• Epoxy flooring
• Pressure washing

```html
<!DOCTYPE html>
<html lang="en">
<head>
<meta charset="utf-8">
<title>Mesa Hue — Business Cards</title>
<link href="https://fonts.googleapis.com/css2?family=Montserrat:wght@400;500;600&display=swap" rel="stylesheet">
<style>
  :root {
    --bg: #2a2a2c;
    --card: #f4f4f4;
    --card-edge: #e6e6e6;
    --ink: #2b2b2b;
    --ink-soft: #6a6a6a;
    --rule: #3a3a3a;
    --accent: #7a4fb3;
  }
  * { box-sizing: border-box; margin: 0; padding: 0; }
  html, body { width: 1200px; height: 900px; overflow: hidden; }
  body {
    background: var(--bg);
    font-family: "Montserrat", sans-serif;
    color: var(--ink);
    position: relative;
  }
  .card {
    position: absolute;
    left: 250px;
    width: 700px;
    height: 400px;
    background: linear-gradient(160deg, #fafafa, var(--card) 60%, var(--card-edge));
    border-radius: 26px;
    overflow: hidden;
  }
  .card--front { top: 40px; }
  .card--back { top: 460px; }

  .brand { position: absolute; display: flex; flex-direction: column; align-items: flex-start; }
  .brand__row { display: flex; align-items: center; gap: 12px; }
  .brand__mark { width: 22px; height: 22px; background: var(--accent); flex: none; }
  .brand__name {
    font-size: 36px; font-weight: 600; letter-spacing: 3px;
    color: var(--accent); line-height: 1; white-space: nowrap;
  }
  .brand__tagline {
    margin-top: 10px; font-size: 10.5px; font-weight: 400;
    color: var(--ink-soft); letter-spacing: 0.3px; white-space: nowrap;
  }

  /* front */
  .card--front .brand { left: 40px; top: 160px; }
  .front__divider {
    position: absolute; left: 330px; top: 90px;
    width: 1.5px; height: 220px; background: var(--rule);
  }
  .contact { position: absolute; left: 355px; top: 110px; }
  .contact__name { font-size: 21px; font-weight: 500; letter-spacing: 1.5px; text-transform: uppercase; white-space: nowrap; }
  .contact__role { font-size: 14px; color: var(--ink-soft); margin-top: 2px; margin-bottom: 22px; }
  .contact__list { list-style: none; }
  .contact__item {
    display: flex; align-items: center; gap: 12px;
    font-size: 14px; margin-bottom: 12px; white-space: nowrap;
  }
  .contact__icon {
    width: 20px; height: 20px; border-radius: 50%;
    background: var(--ink); display: flex; align-items: center; justify-content: center;
    flex: none;
  }
  .contact__icon svg { width: 12px; height: 12px; }

  /* back */
  .card--back .brand { left: 50px; top: 90px; }
  .back__rule-top {
    position: absolute; left: 0; top: 250px; width: 180px; height: 1.5px; background: var(--rule);
  }
  .guarantee {
    position: absolute; left: 195px; top: 237px;
    display: flex; align-items: center; gap: 12px;
    font-size: 14px; color: var(--ink); white-space: nowrap;
  }
  .guarantee__badge {
    width: 26px; height: 26px; border-radius: 50%;
    border: 2px solid var(--ink); background: #dcdcdc;
  }
  .back__rule-bottom {
    position: absolute; left: 200px; top: 330px; width: 500px; height: 1.5px; background: var(--rule);
  }
  .services { position: absolute; left: 420px; top: 60px; list-style: none; }
  .services__item {
    display: flex; align-items: center; gap: 10px;
    font-size: 14px; margin-bottom: 9px; white-space: nowrap;
  }
  .services__tick {
    width: 18px; height: 18px; border-radius: 50%;
    border: 1.5px solid var(--ink); display: flex; align-items: center; justify-content: center; flex: none;
  }
  .services__tick svg { width: 10px; height: 10px; }
</style>
</head>
<body>

  <section class="card card--front" aria-label="Business card front">
    <div class="brand">
      <div class="brand__row">
        <span class="brand__mark"></span>
        <span class="brand__name">MESA HUE</span>
      </div>
      <span class="brand__tagline">Commercial | Residential | Interior | Exterior</span>
    </div>

    <div class="front__divider"></div>

    <div class="contact">
      <h1 class="contact__name">Dorian Vakelby</h1>
      <p class="contact__role">Owner</p>
      <ul class="contact__list">
        <li class="contact__item">
          <span class="contact__icon"><svg viewBox="0 0 12 12"><path d="M3 1.5 L4.6 1.5 L5.3 3.6 L4.3 4.4 C4.9 5.7 6 6.8 7.4 7.5 L8.2 6.5 L10.3 7.2 L10.3 8.8 C10.3 9.5 9.7 10 9 10 C5.3 9.7 2.3 6.7 2 3 C2 2.2 2.4 1.5 3 1.5 Z" fill="#fff"/></svg></span>
          382.516.2074
        </li>
        <li class="contact__item">
          <span class="contact__icon"><svg viewBox="0 0 12 12"><rect x="1.5" y="3" width="9" height="6" fill="none" stroke="#fff" stroke-width="1.2"/><path d="M1.5 3 L6 6.5 L10.5 3" fill="none" stroke="#fff" stroke-width="1.2"/></svg></span>
          mesahuepainting@mailbox.example
        </li>
        <li class="contact__item">
          <span class="contact__icon"><svg viewBox="0 0 12 12"><circle cx="6" cy="6" r="4.3" fill="none" stroke="#fff" stroke-width="1.1"/><ellipse cx="6" cy="6" rx="1.8" ry="4.3" fill="none" stroke="#fff" stroke-width="1"/><line x1="1.7" y1="6" x2="10.3" y2="6" stroke="#fff" stroke-width="1"/></svg></span>
          mesahuepainting.example
        </li>
        <li class="contact__item">
          <span class="contact__icon"></span>
          /mesahuepainting
        </li>
      </ul>
    </div>
  </section>

  <section class="card card--back" aria-label="Business card back">
    <div class="brand">
      <div class="brand__row">
        <span class="brand__mark"></span>
        <span class="brand__name">MESA HUE</span>
      </div>
      <span class="brand__tagline">Commercial | Residential | Interior | Exterior</span>
    </div>

    <div class="back__rule-top"></div>
    <div class="guarantee">
      <span class="guarantee__badge"></span>
      <span>100% customer satisfaction guaranteed</span>
    </div>
    <div class="back__rule-bottom"></div>

    <ul class="services">
      <li class="services__item"><span class="services__tick"><svg viewBox="0 0 10 10"><path d="M2 5.2 L4.2 7.3 L8 2.8" fill="none" stroke="#2b2b2b" stroke-width="1.4"/></svg></span>Interior/exterior painting</li>
      <li class="services__item"><span class="services__tick"><svg viewBox="0 0 10 10"><path d="M2 5.2 L4.2 7.3 L8 2.8" fill="none" stroke="#2b2b2b" stroke-width="1.4"/></svg></span>Drywall repair/texture</li>
      <li class="services__item"><span class="services__tick"><svg viewBox="0 0 10 10"><path d="M2 5.2 L4.2 7.3 L8 2.8" fill="none" stroke="#2b2b2b" stroke-width="1.4"/></svg></span>Fence staining/refinishing</li>
      <li class="services__item"><span class="services__tick"><svg viewBox="0 0 10 10"><path d="M2 5.2 L4.2 7.3 L8 2.8" fill="none" stroke="#2b2b2b" stroke-width="1.4"/></svg></span>Concrete staining</li>
      <li class="services__item"><span class="services__tick"><svg viewBox="0 0 10 10"><path d="M2 5.2 L4.2 7.3 L8 2.8" fill="none" stroke="#2b2b2b" stroke-width="1.4"/></svg></span>Epoxy flooring</li>
      <li class="services__item"><span class="services__tick"><svg viewBox="0 0 10 10"><path d="M2 5.2 L4.2 7.3 L8 2.8" fill="none" stroke="#2b2b2b" stroke-width="1.4"/></svg></span>Pressure washing</li>
    </ul>
  </section>

</body>
</html>
```